Snapnook needs You

Help us create an inviting, amazing, sleek, simple, clear landing page for a picture-memory-social connection site!

Business Name: SnapNook
Industry: Social Networking and Creativity through Pictures
A web platform for and about a community that is driven by a passion for sharing, caring, bonding, collaborating, creating and earning with pictures, through pictures and other related creative activities. This is going to be a great site for all creative artists-photographers, artists, graphic artists to express their work and their creativity.

The main focus of the site is - CONNECTIONS.
This will be uncoded.

Desired Website Screen Size
1024x768... Widescreen/Landscape orientation, is what we mean... So it fits on a CPU screen.

Desired look and feel and message
Look: Visitor should feel immersed in the page, in the world the page creates, simple, elegant, sophisticated, contemporary. We really like a clean uncluttered look.

Special mention: By the way we love the marketing genius who thought up this branding for velu yogurt where they used the two dots above the o to create a branding effect that made this brand instantly identifiable. http://www.velu-dairy.ca/en/

The two dots by themselves without having even the name present brings up the whole brand now. The dots are used above all the ingredients of the yogurt creating friendly figures, and above people in commercials-bringing the people onto the side of "team" velu. Snapnook may have a character created or something distinctive in the letters in the name created to brand the site as well.

Feel: Engaging; Magical without being corny, here is a link to give an example look and feel but please do not be hindered in your creativity by this suggestion. We love all creative angles.
http://artscrapheap.com/graphic/5820317-camera-film-roll-blue-background

Message: Life and memories and connections through pictures.

Target audience:
The site is focused on pictures but not confined to photography enthusiasts (although they are an integral part of the site). Customers/Visitors will include families, corporates and the younger generation - all age groups, all class, everyone with pictures to express, memories to share.

Website design we like:
http://morvantstudio.com/work/northern-ballet-guild/
http://morvantstudio.com/work/pixelhop/

What colors do we want to see on our landing page?
We would like the background to be grey or blue since it is grey is picture neutral colour and blue highlights pictures well and we also like blue and silver, which can be integrated into the theme. Also like green. But please do not let these instructions limit your creativity. We are open to new ideas and colours.

Predetermined Concepts if any:
We have a concept in mind and we think it would be cool to have an interface for the user through the back of a camera on the landing page -This could be used to create a scene or world the visitor feels a part of or is immersed into. The back screen of the camera may act as a screen for the slideshow of featured pictures on the site.

Content on the Page:
Photo Gallery with full screen, thumbnail view, zoom option etc.
Prominent but short introductory message
Sign in / Login Options
Links: Home Page; About; Info/Help; Contact Us; Privacy Policy; Terms of Use
At the bottom of the page: Follow Me/Like/Workfolio...social buttons.

Please feel free to add any other element to the landing page that you think might add to the effect of simple yet amazing look -clean, simple, uncluttered, sophisticated, stylish, inviting and engaging.
The concept is a guideline, but we would like you to be as creative as you can, even if it meant stepping out of these guidelines - rethink design, style, content if you like. We believe in bringing a solution in an innovative yet simple and elegant style. Something a visitor would be intrigued enough to explore and the guest would feel comfortable enough taking that step forward to have fun on the site. If you believe in the same, and you have the skill then you will have what we need. Good luck, go for it and we are excited to see what the amazing designers on this amazing site have to offer.
If you have any questions please free to ask.
Updates

HI wanted to send an update that this project design has been guaranteed.

Our site will be one to celebrate and showcase imagination as well as connection.  We would love to see what you create. Keep in mind our site will showcase all creativity, photographs, artists, graphic artists so this would be a benefit you may want to take advantage of in the future, a place where, if you so choose, you could gain exposure for your work. Therefore, even if you do not win the design project there is possible future benefit.

Imagination is everything.
Imagination encircles the world.-Harwood

Reason: We are giving the designers who accepted invites but have not yet submitted a chance to finish their submissions and the ones who are working on revisions a chance to finish those:)

Hello everyone,

Due to time constraints we must come to a decision sooner than the deadline of 28th. 

So, please try to submit any new designs or modifications to the old ones before the 26th. We are very thankful to all of you who have participated - for your designs, enthusiasm and kind words. 

Good luck! :)

• Thank you for the interest shown and your submissions! Designers who have submitted up until now have shown great potential. We are VERY excited with the quality of work and designs.

We want to add that Snapnook is not exclusively for the photographers. The site is for every person who may have a picture to store, organise, use or share - whether publicly or with only a few friends and family.

Snapnook is about allowing people to take control of their creativity. It is about providing tools to our users so that they can build their own connections and social network... of friends, family, fans, clients, ideas, thoughts, emotions etc. through pictures without worrying about their privacy or control over their creations.

With this update we want to encourage others to go beyond the camera theme. Do not let us restrict your creativity. Let YOUR OWN ideas take over if that’s what you think will best convey the message and will appeal to the users.

```html
<!DOCTYPE html>
<html lang="en">
<head>
<meta charset="utf-8">
<title>SnapNook — Life, memories &amp; connections through pictures</title>
<link rel="stylesheet" href="https://fonts.googleapis.com/css2?family=Quicksand:wght@300;400;500&display=swap">
<style>
  :root {
    --leather-top: #2b2a29;
    --leather-bottom: #1b1a19;
    --ink-light: #e9e9e9;
    --ink-soft: #cfcfcf;
    --frame-dark: #3b3b3b;
    --button-green: #2fbf57;
    --button-green-dark: #1c9a3e;
    --band-blue: #2d5f96;
    --band-blue-deep: #1f4677;
    --footer-grey: #e6e6e6;
    --footer-ink: #3a3a3a;
    --thumb-border: #ececec;
    --icon-ring: #f2f2f2;
    --icon-teal: #35c8e0;
  }
  * { box-sizing: border-box; margin: 0; padding: 0; }
  html, body { width: 1200px; height: 900px; overflow: hidden; }
  body {
    position: relative;
    font-family: "Quicksand", sans-serif;
    background: var(--leather-bottom);
  }
  .stage {
    position: absolute; left: 0; top: 0; width: 1200px; height: 594px;
    background: radial-gradient(ellipse at 50% 30%, var(--leather-top), var(--leather-bottom) 80%);
  }
  .brand {
    position: absolute; left: 38px; top: 14px;
    font-size: 42px; font-weight: 400; color: #fff; letter-spacing: 1px;
  }
  .account { position: absolute; top: 32px; left: 904px; display: flex; gap: 16px; }
  .account a {
    display: block; width: 89px; height: 24px; line-height: 24px; text-align: center;
    border-radius: 7px; color: #fff; text-decoration: none;
    font: 14px Arial, Helvetica, sans-serif;
    background: linear-gradient(var(--button-green), var(--button-green-dark));
    box-shadow: 0 2px 3px rgba(0,0,0,.6);
  }
  .side-nav { position: absolute; left: 20px; top: 130px; width: 80px; }
  .side-nav a {
    position: absolute; left: 0; width: 80px; text-align: center;
    color: var(--ink-light); text-decoration: none; font: 14px Arial, Helvetica, sans-serif;
  }
  .side-nav svg { display: block; margin: 0 auto 4px; }
  .showcase {
    position: absolute; left: 117px; top: 101px; width: 776px; height: 401px;
    background: var(--frame-dark); padding: 8px;
    box-shadow: 0 4px 10px rgba(0,0,0,.7);
  }
  .showcase-photo {
    width: 100%; height: 100%;
    background: linear-gradient(180deg, #1d2a44 0%, #4a4863 30%, #c0705a 55%, #2b2a35 72%, #0e1220 100%);
  }
  .slider-controls { position: absolute; left: 789px; top: 520px; display: flex; gap: 4px; }
  .slider-controls button {
    width: 44px; height: 28px; border: 1px solid #555; border-radius: 14px 4px 4px 14px;
    background: linear-gradient(#222, #050505); cursor: pointer;
  }
  .slider-controls button + button { border-radius: 4px 14px 14px 4px; }
  .intro { position: absolute; left: 913px; top: 102px; width: 275px; }
  .intro h1 {
    font-weight: 300; font-size: 23px; line-height: 23.5px; letter-spacing: 1.6px;
    color: var(--ink-soft); text-transform: uppercase; margin-bottom: 10px;
  }
  .intro p { font-size: 13.5px; line-height: 18px; color: var(--ink-soft); letter-spacing: .4px; }
  .gallery-band {
    position: absolute; left: 0; top: 594px; width: 1200px; height: 247px;
    background: radial-gradient(ellipse at 50% 20%, var(--band-blue), var(--band-blue-deep) 90%);
  }
  .thumb {
    position: absolute; top: 29px; width: 200px; height: 152px;
    border: 6px solid var(--thumb-border);
    box-shadow: 0 6px 10px rgba(0,0,0,.45);
  }
  .thumb-hands  { left: 28px;  background: radial-gradient(circle at 45% 55%, #4a5a6a, #111 60%); }
  .thumb-green  { left: 261px; background: #3fbf6c; }
  .thumb-beach  { left: 495px; background: linear-gradient(#b9d1e8 0%, #e7eef5 45%, #7d9cae 55%, #d8ccb0 75%, #c4b698 100%); }
  .thumb-stack  { left: 728px; background: linear-gradient(160deg, #e5f0b0, #bcd67a 60%, #6c8a45); }
  .thumb-cookie { left: 960px; background: radial-gradient(circle at 60% 60%, #f0deb3, #c49a62 55%, #6d4a2c); }
  .site-footer {
    position: absolute; left: 0; top: 841px; width: 1200px; height: 59px;
    background: var(--footer-grey); color: var(--footer-ink);
    font: 12px Arial, Helvetica, sans-serif;
  }
  .copyright { position: absolute; left: 30px; top: 21px; }
  .legal { position: absolute; left: 292px; top: 21px; display: flex; gap: 12px; }
  .legal a, .social a { color: var(--footer-ink); text-decoration: none; }
  .social { position: absolute; right: 22px; top: 20px; display: flex; gap: 14px; }
  .social a { display: flex; align-items: center; gap: 5px; }
  .social a::before {
    content: ""; width: 12px; height: 12px; border-radius: 50%; background: #2f6aa6;
  }
</style>
</head>
<body>
  <header class="stage">
    <div class="brand">SnapNook</div>
    <nav class="account">
      <a href="#">Log in</a>
      <a href="#">Sign Up</a>
    </nav>

    <nav class="side-nav">
      <a href="#" style="top:0">
        <svg width="36" height="36" viewBox="0 0 36 36"><circle cx="18" cy="18" r="16" fill="#000" stroke="var(--icon-ring)" stroke-width="2"/><path d="M9 18 L18 10 L27 18 Z" fill="#fff"/><rect x="12" y="18" width="12" height="8" fill="#fff"/></svg>
        Home
      </a>
      <a href="#" style="top:72px">
        <svg width="36" height="36" viewBox="0 0 36 36"><circle cx="18" cy="18" r="16" fill="#000" stroke="var(--icon-ring)" stroke-width="2"/><text x="18" y="22.5" text-anchor="middle" font-family="Arial, sans-serif" font-weight="700" font-size="12" fill="var(--icon-teal)">SN</text></svg>
        About
      </a>
      <a href="#" style="top:140px">
        <svg width="36" height="36" viewBox="0 0 36 36"><circle cx="18" cy="18" r="16" fill="#000" stroke="var(--icon-ring)" stroke-width="2"/><text x="18" y="25" text-anchor="middle" font-family="Georgia, serif" font-style="italic" font-weight="700" font-size="20" fill="#fff">i</text></svg>
        Info
      </a>
      <a href="#" style="top:222px">
        <svg width="36" height="36" viewBox="0 0 36 36"><circle cx="18" cy="18" r="16" fill="#000" stroke="var(--icon-ring)" stroke-width="2"/><rect x="10" y="13" width="16" height="11" fill="#fff"/><path d="M10 13 L18 20 L26 13" fill="none" stroke="#000" stroke-width="1.5"/></svg>
        Contact Us
      </a>
    </nav>

    <div class="showcase">
      <div class="showcase-photo" role="img" aria-label="Featured photo: a lit stone bridge with twin towers over a river at dusk"></div>
    </div>

    <div class="slider-controls">
      <button aria-label="Previous"><svg width="20" height="16" viewBox="0 0 20 16"><path d="M16 1 L3 8 L16 15 Z" fill="#fff"/></svg></button>
      <button aria-label="Next"><svg width="20" height="16" viewBox="0 0 20 16"><path d="M4 1 L17 8 L4 15 Z" fill="#fff"/></svg></button>
    </div>

    <section class="intro">
      <h1>Life, memories &amp; connections through pictures</h1>
      <p>Lorem ipsum dolor sit amet, consectetur adipiscing elit. Aliquam accumsan sagittis velit. Fusce a augue nisl. Cras scelerisque porttitor arcu, at malesuada nulla rutrum sed. Curabitur quis massa massa, at auctor nunc. Phasellus pellentesque aliquam libero vel tincidunt. Integer id dolor id elit elementum rhoncus.</p>
    </section>
  </header>

  <section class="gallery-band">
    <div class="thumb thumb-hands" role="img" aria-label="Hands cupping a small globe on black"></div>
    <div class="thumb thumb-green" role="img" aria-label="Two pastel giraffe figures on green"></div>
    <div class="thumb thumb-beach" role="img" aria-label="A person sitting on a sandy beach by the sea"></div>
    <div class="thumb thumb-stack" role="img" aria-label="A stack of pale green macarons"></div>
    <div class="thumb thumb-cookie" role="img" aria-label="Close-up of a chocolate chip cookie"></div>
  </section>

  <footer class="site-footer">
    <span class="copyright">© 2012 SnapNook All Rights Reserved</span>
    <nav class="legal"><a href="#">Privacy Policy</a><a href="#">Terms &amp; Conditions</a></nav>
    <nav class="social">
      <a href="#">Friendwall</a>
      <a href="#">Chirpline</a>
      <a href="#">Workfolio</a>
      <a href="#">Blogreel</a>
    </nav>
  </footer>
</body>
</html>
```